Jewelry Shop Needs a Business Card Design

***We want a very sharp and unforgettable pantone for the Business Card. ***
***We do not want the business card or logo only in black, white and grey color!!!Please provide us a main color as our brand topic! Thanks!! ***

Mabel’s Nook is a Hong Kong based fine jewelry brand.

We want a very nice, simple and elegant business card design for Mabel's Nook Brand. The company's logo has been uploaded already.

You can design with below info:

Dorian Fung
Director
M: +852 94273658
T: +852 35820417
F: +852 35820419
E: dorian.fung@mabelsnook.example
5/F , Harbourlight Tower, 12-18 Orchid Lane, Wan Tung Kok, Kowloon, Hong Kong

Target Market(s)

Mabel’s Nook philosophy is a jewelry icon of young, creative, trendy, fashionable, stylish, energetic, and elegant. For Mabel’s Nook, jewelry is one collection of artworks, the most important items in personal life.

Industry/Entity Type

Jewelry

Requirements
Must have
• We want a very sharp and unforgettable pantone for the Business Card.

```html
<!DOCTYPE html>
<html lang="en">
<head>
<meta charset="utf-8">
<title>Mabel’s Nook – Business Card</title>
<link rel="stylesheet" href="https://fonts.googleapis.com/css2?family=Cinzel:wght@500&family=Open+Sans:wght@600&family=Tinos&display=swap">
<style>
  :root {
    --brand: #8a0035;
    --brand-arc: #85002f;
    --paper: #ffffff;
    --ink-light: #ffffff;
  }
  html, body {
    margin: 0;
    padding: 0;
    width: 1200px;
    height: 849px;
    overflow: hidden;
    background: var(--paper);
  }
  .canvas {
    position: relative;
    width: 1200px;
    height: 849px;
  }
  .card {
    position: absolute;
    left: 110px;
    width: 480px;
    height: 267px;
    background: var(--brand);
    overflow: hidden;
    color: var(--ink-light);
  }
  .card--front { top: 141px; }
  .card--back { top: 439px; }

  .card__arc {
    position: absolute;
    left: 0;
    top: 0;
  }

  .holder {
    position: absolute;
    left: 0;
    top: 100px;
    width: 228px;
    text-align: center;
  }
  .holder__name {
    margin: 0;
    font-family: "Cinzel", serif;
    font-weight: 500;
    font-size: 25px;
    line-height: 1;
    white-space: nowrap;
  }
  .holder__role {
    margin: 12px 0 0;
    font-family: "Tinos", serif;
    font-size: 18px;
    line-height: 1;
  }

  .brand-lockup {
    position: absolute;
    display: flex;
    flex-direction: column;
    align-items: center;
  }
  .brand-lockup__disc {
    border-radius: 50%;
    background: var(--paper);
  }
  .brand-lockup__name {
    font-family: "Tinos", serif;
    font-weight: 400;
    white-space: nowrap;
    line-height: 1;
    color: var(--ink-light);
  }
  .card--front .brand-lockup {
    left: 263px;
    top: 24px;
    width: 180px;
  }
  .card--front .brand-lockup__disc { width: 84px; height: 84px; }
  .card--front .brand-lockup__name {
    margin-top: 12px;
    font-size: 17px;
    letter-spacing: 0.8px;
  }
  .card--back .brand-lockup {
    left: 0;
    top: 37px;
    width: 480px;
  }
  .card--back .brand-lockup__disc { width: 152px; height: 152px; }
  .card--back .brand-lockup__name {
    margin-top: 22px;
    font-size: 28px;
    letter-spacing: 1.4px;
  }

  .contact {
    position: absolute;
    left: 0;
    top: 0;
    margin: 0;
    padding: 0;
    list-style: none;
    font-family: "Open Sans", sans-serif;
    font-weight: 600;
    font-size: 11.6px;
    line-height: 16px;
  }
  .contact li {
    position: absolute;
    white-space: nowrap;
  }
</style>
</head>
<body>
<main class="canvas">

  <section class="card card--front" aria-label="Business card, front">
    <svg class="card__arc" width="480" height="267" viewBox="0 0 480 267" aria-hidden="true">
      <defs>
        <filter id="arc-shadow" x="-20%" y="-20%" width="140%" height="140%">
          <feDropShadow dx="4" dy="2" stdDeviation="4" flood-color="#2a000f" flood-opacity="0.4"/>
        </filter>
      </defs>
      <circle cx="90" cy="130" r="142" fill="var(--brand-arc)" filter="url(#arc-shadow)"/>
    </svg>

    <div class="holder">
      <h1 class="holder__name">Dorian Fung</h1>
      <p class="holder__role">director</p>
    </div>

    <div class="brand-lockup">
      <span class="brand-lockup__disc" aria-hidden="true"></span>
      <span class="brand-lockup__name">Mabel’s Nook</span>
    </div>

    <ul class="contact">
      <li style="left:241px; top:161px;">M: +852 94273658</li>
      <li style="left:235px; top:177px;">T: +852 35820417</li>
      <li style="left:231px; top:193px;">F: +852 35820419</li>
      <li style="left:226px; top:209px;">E: dorian.fung@mabelsnook.example</li>
      <li style="left:216px; top:225px;">5/F , Harbourlight Tower, 12-18 Orchid</li>
      <li style="left:206px; top:241px;">Lane, Wan Tung Kok, Kowloon, Hong Kong</li>
    </ul>
  </section>

  <section class="card card--back" aria-label="Business card, back">
    <div class="brand-lockup">
      <span class="brand-lockup__disc" aria-hidden="true"></span>
      <span class="brand-lockup__name">Mabel’s Nook</span>
    </div>
  </section>

</main>
</body>
</html>
```